Construction Directory Website Flyer

We need a postcard size +/- or somewhere around that size (something standard) flyer designed for our construction directory website. Leave a spot for tagline. Call to action is 'register your company now'. I am thinking many mini pictures of different construction to show that it is for the entire construction industry. Logo and screenshot of the homepage of the website is attached. Use same theme as webpage.

Target Market(s)

Construction Industry

Industry/Entity Type

Construction

Font styles to use
Sans Serif

Requirements
Must have
• Call to action
• Colors to match logo
• Area to add description and details.
Nice to have
• Construction Images
Should not have
• No Cartoonish types of things

```html
<!DOCTYPE html>
<html lang="en">
<head>
<meta charset="utf-8">
<title>BuildLink Hub – Directory Flyer</title>
<link href="https://fonts.googleapis.com/css2?family=Lato:wght@400;700;900&family=Kaushan+Script&display=swap" rel="stylesheet">
<style>
  :root{
    --stage:#e8e5e0;
    --paper:#ffffff;
    --red:#e5321c;
    --red-dark:#c4220f;
    --slate:#56636e;
    --slate-dark:#3e4a54;
    --ink:#1d1f22;
    --logo-ink:#3b444d;
    --sky-top:#cfe3ef;
    --sky-low:#9fbcd0;
    --vest:#c9d84a;
  }
  *{box-sizing:border-box;margin:0;padding:0}
  html,body{width:1200px;height:1000px;overflow:hidden}
  body{background:var(--stage);font-family:"Lato",Arial,sans-serif;position:relative}

  .flyer{
    position:absolute;left:230px;top:25px;width:740px;height:950px;
    background:var(--paper);overflow:hidden;
    box-shadow:0 6px 22px rgba(0,0,0,.25);
  }
  .hero{position:absolute;left:0;top:0;width:740px;height:560px}

  .brand{
    position:absolute;left:452px;top:26px;display:flex;align-items:center;gap:12px;
  }
  .brand-square{width:50px;height:50px;background:var(--red)}
  .brand-name{
    font-family:"Lato",Arial,sans-serif;font-weight:700;font-size:29px;line-height:30px;
    color:var(--logo-ink);
  }

  .tagline{
    position:absolute;right:26px;top:408px;text-align:right;
    font-family:"Lato",Arial,sans-serif;font-weight:900;font-size:30px;line-height:30px;
    color:var(--red);text-transform:uppercase;letter-spacing:-.3px;
    text-shadow:-2px 0 #fff,2px 0 #fff,0 -2px #fff,0 2px #fff,1px 1px #fff,-1px -1px #fff,1px -1px #fff,-1px 1px #fff;
  }

  .gallery-item{
    position:absolute;border-radius:50%;border:5px solid #fff;
    box-shadow:0 2px 6px rgba(0,0,0,.35);
  }
  .gallery-item.house{left:-4px;top:365px;width:156px;height:156px;background:linear-gradient(160deg,#7fb2dd,#d9dde0 60%,#a98f70)}
  .gallery-item.crew{left:135px;top:448px;width:144px;height:144px;background:linear-gradient(170deg,#8f9a6c,#6b6d57 55%,#3e3f38)}
  .gallery-item.carpenter{left:273px;top:481px;width:156px;height:156px;background:linear-gradient(150deg,#6f8f6a,#b58a62 55%,#4d4438)}
  .gallery-item.tower{left:429px;top:499px;width:176px;height:176px;background:linear-gradient(180deg,#2f6f8a,#4b8aa0 45%,#6a5a52)}
  .gallery-item.excavator{left:588px;top:520px;width:156px;height:156px;background:linear-gradient(170deg,#4f4f4a,#8a8a80 45%,#c9503a 70%,#6b6355)}

  .description{
    position:absolute;left:22px;top:586px;width:700px;
    font-size:14.6px;line-height:17.6px;color:var(--ink);
    text-align:justify;hyphens:auto;
  }
  .wrap-guard{float:right;clear:right}
  .wrap-guard.g1{width:590px;height:52px}
  .wrap-guard.g2{width:482px;height:35px}
  .wrap-guard.g3{width:400px;height:18px}
  .wrap-guard.g4{width:160px;height:18px}
  .description .lead{letter-spacing:3px}
  .description p+p{margin-top:0}

  .cta{
    position:absolute;left:0;right:0;top:840px;text-align:center;
    font-family:"Kaushan Script","Brush Script MT",cursive;font-size:31px;color:var(--red);
  }

  .contact-bar{
    position:absolute;left:0;bottom:0;width:740px;height:62px;
    background:linear-gradient(180deg,var(--slate),var(--slate-dark));
    display:flex;align-items:center;justify-content:space-between;padding:0 26px;
  }
  .contact-item{display:flex;align-items:center;gap:9px;color:#fff;font-size:13.5px}
  .contact-icon{width:26px;height:26px;border-radius:50%;background:#fff;display:flex;align-items:center;justify-content:center}
  .contact-icon svg{width:15px;height:15px;fill:var(--slate-dark)}
</style>
</head>
<body>
<main class="flyer">
  <svg class="hero" viewBox="0 0 740 560" aria-hidden="false">
    <defs>
      <linearGradient id="skyFill" x1="0" y1="0" x2="0.4" y2="1">
        <stop offset="0" stop-color="var(--sky-top)"/>
        <stop offset=".55" stop-color="#b8cfdd"/>
        <stop offset="1" stop-color="#8d9ea6"/>
      </linearGradient>
      <linearGradient id="crewFill" x1="0" y1="0" x2="1" y2="0">
        <stop offset="0" stop-color="#4d6fa8" stop-opacity=".75"/>
        <stop offset=".55" stop-color="var(--vest)" stop-opacity=".55"/>
        <stop offset="1" stop-color="var(--vest)" stop-opacity="0"/>
      </linearGradient>
    </defs>
    <g role="img" aria-label="Photo of three site engineers in hard hats and hi-vis vests reviewing plans, one pointing across the site">
      <path d="M0 0H740V505C560 488 320 430 0 300Z" fill="url(#skyFill)"/>
      <path d="M0 0H480V470C330 420 180 360 0 300Z" fill="url(#crewFill)"/>
    </g>
    <path d="M0 300C320 430 560 488 740 505V522C560 505 300 452 0 330Z" fill="var(--slate)"/>
    <path d="M0 330C300 452 560 505 740 522V540C560 520 300 470 0 356Z" fill="#fff"/>
    <path d="M0 356C300 470 560 520 740 540V546C560 528 300 480 0 366Z" fill="var(--red)"/>
  </svg>

  <div class="brand">
    <span class="brand-square"></span>
    <span class="brand-name">BuildLink<br>Hub</span>
  </div>

  <h2 class="tagline">Built by construction<br>for construction</h2>

  <div class="gallery-item house" role="img" aria-label="Photo of a house frame under construction with scaffolding"></div>
  <div class="gallery-item crew" role="img" aria-label="Photo of a road crew working with equipment"></div>
  <div class="gallery-item carpenter" role="img" aria-label="Photo of a carpenter sawing timber"></div>
  <div class="gallery-item tower" role="img" aria-label="Photo of a high-rise under construction with a tower crane"></div>
  <div class="gallery-item excavator" role="img" aria-label="Photo of an excavator on a building site"></div>

  <section class="description">
    <span class="wrap-guard g1"></span>
    <span class="wrap-guard g2"></span>
    <span class="wrap-guard g3"></span>
    <span class="wrap-guard g4"></span>
    <p><span class="lead">Lorem</span> ipsum dolor sit amet, consectetur adipiscing elit. Quisque id felis sed orci placerat feugiat. Donec tellus elit, rhoncus at mauris non, rutrum convallis augue. Aliquam fringilla ultricies viverra. Proin dictum neque vitae massa fringilla tincidunt. In tincidunt mi quis nulla ultricies tempor. Nam imperdiet bibendum leo in ultricies. In tincidunt nulla eget pellentesque tempus.</p>
    <p>In hac habitasse platea dictumst. Proin a enim sed nisi euismod tristique. Donec malesuada eleifend nunc eu dictum. Morbi faucibus mi ex, sit amet elementum elit pretium eu. Maecenas hendrerit lacus nunc, non tristique libero vestibulum ut. Donec in dapibus ipsum. Quisque eleifend risus ex, et tempor dui varius ut. Vestibulum vestibulum lectus eget mi venenatis, eu laoreet odio tristique.</p>
  </section>

  <p class="cta">Register Your Company Now</p>

  <footer class="contact-bar">
    <span class="contact-item">
      <span class="contact-icon"><svg viewBox="0 0 24 24"><path d="M6.6 10.8a15.1 15.1 0 0 0 6.6 6.6l2.2-2.2c.3-.3.7-.4 1-.2 1.1.4 2.3.6 3.6.6.6 0 1 .4 1 1V20c0 .6-.4 1-1 1A17 17 0 0 1 3 4c0-.6.4-1 1-1h3.5c.6 0 1 .4 1 1 0 1.3.2 2.5.6 3.6.1.3 0 .7-.2 1z"/></svg></span>
      012-555-0148
    </span>
    <span class="contact-item">
      <span class="contact-icon"><svg viewBox="0 0 24 24"><path d="M3 6h18v12H3z M3 6l9 7 9-7" fill="none" stroke="var(--slate-dark)" stroke-width="2.2"/></svg></span>
      info@buildlinkhub.com
    </span>
    <span class="contact-item">
      <span class="contact-icon"><svg viewBox="0 0 24 24"><g fill="none" stroke="var(--slate-dark)" stroke-width="2"><circle cx="12" cy="12" r="9"/><ellipse cx="12" cy="12" rx="4" ry="9"/><path d="M3 12h18M5 7h14M5 17h14"/></g></svg></span>
      www.buildlinkhub.com
    </span>
  </footer>
</main>
</body>
</html>
```